Poster Required for Cafe to promote Catering

I would like a Poster made to advertise that our business does catering.
On the poster we would like it to say:

Did you know that Sunny Ladle does Catering?
We offer Breakfast, Lunch, Morning and Afternoon Tea Options
Come instore to enquire

At the bottom of the flyer, can you please put the contact details:
Phone 0487 602 914
Email tam@sunnyladlecanteen.com

Poster Size A3

I have attached our logo and menu's so you can get a feel for what we like.

Target Market(s)

Hospital Staff: Doctors, Nurses, Admin

Industry/Entity Type

Hospitality

Requirements
Nice to have
• Some pictures of catering. Eg. Gourmet Sandwiches, Sliders
• You could check our instagram page for ideas on what we do..
• @snyladle_qld

```html
<!DOCTYPE html>
<html lang="en">
<head>
<meta charset="utf-8">
<title>Sunny Ladle Catering Poster</title>
<link rel="stylesheet" href="https://fonts.googleapis.com/css2?family=Tinos:wght@400;700&display=swap">
<style>
  :root {
    --cream: #f9f59c;
    --cocoa: #3d3133;
    --cocoa-deep: #3a282c;
    --white: #ffffff;
    --page: #ffffff;
  }
  html, body {
    margin: 0;
    padding: 0;
    width: 1200px;
    height: 1000px;
    overflow: hidden;
    background: var(--page);
  }
  .canvas {
    position: relative;
    width: 1200px;
    height: 1000px;
    font-family: "Tinos", "Times New Roman", serif;
  }
  .poster-shapes {
    position: absolute;
    left: 0;
    top: 0;
  }
  .headline {
    position: absolute;
    left: 388px;
    width: 427px;
    top: 184px;
    margin: 0;
    text-align: center;
    color: var(--cream);
    font-size: 32px;
    font-weight: 700;
    line-height: 38px;
    word-spacing: 4px;
  }
  .offer {
    position: absolute;
    left: 400px;
    width: 403px;
    top: 296px;
    margin: 0;
    text-align: center;
    color: var(--cocoa);
    font-size: 20px;
    font-weight: 700;
    line-height: 22px;
    word-spacing: 2px;
  }
  .brand-name {
    position: absolute;
    left: 452px;
    width: 296px;
    top: 496px;
    margin: 0;
    text-align: center;
    color: var(--white);
    font-size: 42px;
    font-weight: 700;
    line-height: 50px;
    letter-spacing: 2px;
  }
  .call-to-action {
    position: absolute;
    left: 400px;
    width: 403px;
    top: 700px;
    margin: 0;
    text-align: center;
    color: var(--cocoa);
    font-size: 35px;
    font-weight: 700;
    line-height: 40px;
  }
  .contact {
    position: absolute;
    left: 388px;
    width: 427px;
    top: 768px;
    margin: 0;
    padding: 0;
    list-style: none;
    color: var(--cream);
    font-size: 24px;
    font-weight: 700;
  }
  .contact-item {
    display: flex;
    align-items: center;
    height: 30px;
  }
  .contact-phone { padding-left: 106px; }
  .contact-email { padding-left: 16px; }
  .contact-icon {
    width: 24px;
    height: 20px;
    margin-right: 14px;
    flex: none;
  }
</style>
</head>
<body>
<main class="canvas">
  <svg class="poster-shapes" width="1200" height="1000" viewBox="0 0 1200 1000" aria-hidden="true">
    <rect class="poster-sheet" x="365" y="128" width="473" height="730" fill="var(--cream)"/>
    <rect class="poster-frame-line" x="379" y="145" width="446" height="700" rx="4" fill="none" stroke="var(--cocoa)" stroke-width="4"/>
    <rect class="poster-panel" x="388" y="153" width="427" height="683" fill="var(--cocoa)"/>
    <polygon class="ribbon ribbon-offer" points="383,285 820,285 801,318 820,352 383,352 402,318" fill="var(--cream)" stroke="var(--cocoa)" stroke-width="3" stroke-linejoin="round"/>
    <circle class="badge-ring" cx="600" cy="523" r="141" fill="var(--cocoa-deep)" stroke="var(--cream)" stroke-width="14"/>
    <polygon class="ribbon ribbon-cta" points="383,687 820,687 801,721 820,755 383,755 402,721" fill="var(--cream)" stroke="var(--cocoa)" stroke-width="3" stroke-linejoin="round"/>
  </svg>

  <h1 class="headline">Did you know the Sunny Ladle does Catering?</h1>
  <p class="offer">We offer Breakfast, Lunch and Morning and Afternoon Tea Options</p>
  <p class="brand-name">Sunny Ladle</p>
  <p class="call-to-action">Come instore to enquire</p>

  <ul class="contact">
    <li class="contact-item contact-phone">
      <svg class="contact-icon" viewBox="0 0 24 20" aria-hidden="true">
        <path d="M2 6 Q12 -1 22 6 L20 9 L16 8 L16 5 Q12 3 8 5 L8 8 L4 9 Z" fill="var(--cream)"/>
        <path d="M7 9 L17 9 L20 18 L4 18 Z" fill="var(--cream)"/>
        <circle cx="12" cy="13" r="2.5" fill="var(--cocoa)"/>
      </svg>
      0487 602 914
    </li>
    <li class="contact-item contact-email">
      <svg class="contact-icon" viewBox="0 0 24 20" aria-hidden="true">
        <rect x="1" y="3" width="22" height="15" fill="var(--cream)"/>
        <path d="M1.5 3.5 L12 12 L22.5 3.5" fill="none" stroke="var(--cocoa)" stroke-width="1.6"/>
        <path d="M1.5 17.5 L9 10 M22.5 17.5 L15 10" fill="none" stroke="var(--cocoa)" stroke-width="1.2"/>
      </svg>
      tam@sunnyladlecanteen.com
    </li>
  </ul>
</main>
</body>
</html>
```